Criminal Defense Law firm Billboard Design

We need a billboard to occupy a board space we have ASAP. Would like it to convey our lawfirm's brand. qrlegalshield.com is our website where you can see the colors we use, blues, etc. We have high rez pictures of both attorneys for you to use, just request them. We would like CRIMINAL AND PROBATION DEFENSE to be prominent on this display. We would also like our primary office # along with a second number for Spanish speakers to be displayed.

Target Market(s)

traffic in Cumming, GA

Industry/Entity Type

attorney-legal

Colors
0054AA
0677BA
7BADD7
CADEEF
E8F1F8

Requirements
Must have
• Awesome design that will attract customers

```html
<!DOCTYPE html>
<html lang="en">
<head>
<meta charset="utf-8">
<title>Quinlan Reyes — Criminal and Probation Defense Billboard</title>
<link href="https://fonts.googleapis.com/css2?family=Bebas+Neue&family=Oswald:wght@400&family=Montserrat:wght@700&display=swap" rel="stylesheet">
<style>
  :root {
    --page: #eef2f6;
    --navy-deep: #121f36;
    --navy: #1b2c49;
    --headline-blue: #4a9be2;
    --band-blue: #5ba0de;
    --band-ink: #13223b;
    --white: #ffffff;
    --rule: #c9d6e6;
  }
  * { margin: 0; padding: 0; box-sizing: border-box; }
  html, body {
    width: 1200px; height: 1045px; overflow: hidden;
    background: var(--page);
  }
  .billboard {
    position: absolute; left: 30px; top: 356px;
    width: 1140px; height: 332px;
    background: linear-gradient(180deg, var(--navy) 0%, var(--navy-deep) 100%);
    overflow: hidden;
    font-family: 'Bebas Neue', sans-serif;
  }
  .brand {
    position: absolute; left: 268px; top: 40px; width: 380px;
    text-align: center; color: var(--white);
    font-family: 'Oswald', sans-serif;
  }
  .brand-name {
    font-size: 34px; font-weight: 400; letter-spacing: 6px; line-height: 1;
  }
  .brand-tagline {
    margin-top: 8px; font-size: 12px; letter-spacing: 3px; font-weight: 400;
  }
  .rule {
    position: absolute; left: 42px; width: 701px; height: 2px;
    background: var(--rule);
  }
  .rule-top { top: 131px; }
  .rule-bottom { top: 209px; }
  .headline {
    position: absolute; left: 42px; top: 133px; width: 701px;
    text-align: center; color: var(--headline-blue);
    font-size: 64px; font-weight: 400; line-height: 76px;
    letter-spacing: 0.5px; white-space: nowrap;
  }
  .subline {
    position: absolute; left: 42px; top: 216px; width: 701px;
    text-align: center; color: var(--white);
    font-size: 31px; font-weight: 400; line-height: 34px;
    letter-spacing: 0.5px; white-space: nowrap;
  }
  .contact-band {
    position: absolute; left: 0; top: 256px; width: 100%; height: 76px;
    background: var(--band-blue);
  }
  .website {
    position: absolute; left: 32px; top: 276px;
    color: var(--band-ink); font-size: 30px; line-height: 34px; letter-spacing: 1px;
    white-space: nowrap;
  }
  .phone-icon {
    position: absolute; left: 258px; top: 276px; width: 34px; height: 34px;
  }
  .phone-main, .phone-spanish {
    position: absolute; color: var(--white);
    font-size: 40px; line-height: 42px; white-space: nowrap;
  }
  .phone-main { left: 304px; top: 273px; }
  .divider {
    position: absolute; left: 530px; top: 272px; width: 2px; height: 42px;
    background: rgba(255,255,255,0.7);
  }
  .spanish-label {
    position: absolute; left: 554px; top: 266px;
    font-family: 'Montserrat', sans-serif; font-weight: 700;
    font-size: 13px; letter-spacing: 1px; color: var(--white);
  }
  .phone-spanish { left: 552px; top: 284px; }
  .attorneys-photo {
    position: absolute; left: 790px; top: 34px; width: 305px; height: 298px;
    background: linear-gradient(160deg, #3f5f95 0%, #22427a 55%, #1a3566 100%);
    border-radius: 40px 40px 0 0;
  }
</style>
</head>
<body>
  <section class="billboard">
    <div class="brand">
      <div class="brand-name">QUINLAN | REYES</div>
      <div class="brand-tagline">ATTORNEYS AT LAW</div>
    </div>

    <div class="rule rule-top"></div>
    <h1 class="headline">CRIMINAL AND PROBATION DEFENSE</h1>
    <div class="rule rule-bottom"></div>
    <p class="subline">40 COMBINED YEARS OF EXPERIENCE IN CRIMINAL DEFENSE</p>

    <div class="contact-band"></div>
    <div class="website">QRLEGALSHIELD.COM</div>
    <svg class="phone-icon" viewBox="0 0 34 34" aria-hidden="true">
      <circle cx="17" cy="17" r="17" fill="#13223b"/>
      <path d="M12.5 8.5c.8-.5 1.8-.3 2.3.5l1.6 2.6c.4.7.3 1.6-.3 2.1l-1.3 1.1c.9 1.9 2.4 3.5 4.4 4.5l1.1-1.3c.5-.6 1.4-.8 2.1-.4l2.6 1.5c.8.5 1.1 1.5.6 2.3l-.8 1.4c-.7 1.200-2.2 1.8-3.5 1.3-5-1.8-8.9-5.7-10.600-10.700-.4-1.300.1-2.800 1.3-3.5z" fill="#ffffff"/>
    </svg>
    <div class="phone-main">(770) 555-0182</div>
    <div class="divider"></div>
    <div class="spanish-label">SE HABLA ESPAÑOL</div>
    <div class="phone-spanish">(770) 555-0182</div>

    <div class="attorneys-photo" role="img" aria-label="Photo of the two firm attorneys in suits, arms crossed"></div>
  </section>
</body>
</html>
```